Verdant Rooms Stationary Set

Verdant Rooms is a bespoke interior design firm set to provide services to VIP clients with elegance and minimalism is the main theme for our stationary set. We require a full stationary set covering A4 letterhead, A4 & A3 envelopes, business cards, USB's, CDs, email signature and any other item the designer sees fit. logo is already designed and finalized, and we require the designer to use it as is without modifying the logo.

Address to be used on letterhead / business cards ...etc shall be as follows:

Phone : +971 2 518 3076
P.O. Box : 318947
Address: Block C&D, Bldg. 27, Court 14, Abu Dhabi, United Arab Emirates
Website: www.verdantrooms.example

Target Market(s)

VIP Clients

Industry/Entity Type

Interior Design

Font styles to use
Other font styles liked:
• something to be unique

Colors

Designer to choose colors to be used in the design.

Requirements
Must have
• Elegant, minimalistic
Nice to have
• Simple yet elegant design having a sharp yet clean cut format
Should not have
• No additional colours, just colours that are used in the logo (silver, black or gold)

```html
<!DOCTYPE html>
<html lang="en">
<head>
<meta charset="utf-8">
<title>Verdant Rooms — Envelope Set</title>
<link href="https://fonts.googleapis.com/css2?family=Montserrat:wght@300;400&display=swap" rel="stylesheet">
<style>
  :root {
    --backdrop: #6d6d6d;
    --paper: #3c3c3c;
    --paper-flap: #383838;
    --paper-edge: #2c2c2c;
    --emboss: #343434;
    --gold: #cdb680;
  }
  * { margin: 0; padding: 0; box-sizing: border-box; }
  html, body { width: 1200px; height: 1038px; overflow: hidden; }
  body {
    background: var(--backdrop);
    font-family: "Montserrat", Arial, sans-serif;
    position: relative;
  }
  .envelope {
    position: absolute;
    width: 640px;
    height: 320px;
    background: var(--paper);
    box-shadow: 0 2px 0 var(--paper-edge);
    overflow: hidden;
  }
  .envelope--back { left: 110px; top: 100px; }
  .envelope--front { left: 450px; top: 590px; }

  .envelope__flap {
    position: absolute;
    inset: 0;
    width: 100%;
    height: 100%;
  }
  .brand-name {
    position: absolute;
    z-index: 2;
    color: var(--gold);
    font-weight: 400;
    letter-spacing: 0.14em;
    text-transform: uppercase;
    white-space: nowrap;
  }
  .envelope--back .brand-name {
    top: 44px;
    left: 50%;
    transform: translateX(-50%);
    font-size: 13px;
  }
  .envelope--front .brand-name {
    left: 56px;
    bottom: 52px;
    font-size: 18px;
  }
  .emboss-name {
    position: absolute;
    z-index: 1;
    left: 30px;
    bottom: 18px;
    color: var(--emboss);
    font-weight: 300;
    font-size: 150px;
    line-height: 1;
    letter-spacing: 0.02em;
    white-space: nowrap;
    text-shadow: 0 1px 0 #444444;
  }
  .return-address {
    position: absolute;
    left: 0;
    right: 0;
    top: 232px;
    text-align: center;
    color: var(--gold);
    font-weight: 300;
    font-size: 10px;
    line-height: 1.5;
    letter-spacing: 0.02em;
  }
  .return-address__mark {
    display: block;
    width: 14px;
    height: 4px;
    margin: 0 auto 22px;
    background: var(--gold);
  }
</style>
</head>
<body>

  <section class="envelope envelope--back" aria-label="Envelope, back">
    <svg class="envelope__flap" viewBox="0 0 640 320" aria-hidden="true">
      <path d="M0 0 H640 V16 Q640 28 628 30 L12 140 Q0 142 0 130 Z" fill="var(--paper-flap)"/>
      <path d="M0 132 Q0 142 12 140 L628 30 Q640 28 640 16" fill="none" stroke="#262626" stroke-width="2"/>
    </svg>
    <span class="brand-name">Verdant Rooms</span>
    <p class="return-address">
      <span class="return-address__mark"></span>
      Block C&amp;D, Bldg. 27, Court 14, Abu Dhabi, United Arab Emirates<br>
      P.O. Box: 318947 . www.verdantrooms.example
    </p>
  </section>

  <section class="envelope envelope--front" aria-label="Envelope, front">
    <span class="emboss-name" aria-hidden="true">Verdant</span>
    <span class="brand-name">Verdant Rooms</span>
  </section>

</body>
</html>
```